Silver Creek Plumbing Business card & letter head design

We need a new business card and letter head for our plumbing company called silver creek plumbing. attached is the companys logo. We provide domestic and commercial plumbing services in regional western Australia. We are after Something simple yet nice to look at and something that fits within the trade industry.

Target Market(s)

trade/building industry

Contact Information for Business Card

Darl Hensby
Manager
0461 238 574
enquiries@scplumbwork.net.au
ABN: 47 381 905 462
PCL: 5187

Domestic & Commercial Plumbing
Tip Truck & Excavator hire

Colors

Designer to choose colors to be used in the design.

```html
<!DOCTYPE html>
<html lang="en">
<head>
<meta charset="utf-8">
<title>Silver Creek Plumbing Letterhead</title>
<link rel="stylesheet" href="https://fonts.googleapis.com/css2?family=Open+Sans:wght@400;600&family=Montserrat:wght@700&display=swap">
<style>
  :root {
    --brand-blue: #1656a5;
    --ink: #3a3a3a;
    --label-blue: #1f5fb0;
    --rule-grey: #555;
    --paper: #ffffff;
    --backdrop: #dcdcde;
  }
  * { margin: 0; padding: 0; box-sizing: border-box; }
  html, body { width: 1200px; height: 1200px; overflow: hidden; }
  body {
    background: var(--backdrop);
    font-family: "Open Sans", sans-serif;
    color: var(--ink);
    position: relative;
  }
  .letterhead {
    position: absolute;
    left: 210px; top: 48px;
    width: 780px; height: 1104px;
    background: linear-gradient(180deg, #ffffff 0%, #f6f6f7 100%);
    box-shadow: 0 2px 6px rgba(0,0,0,0.12);
  }
  .brand-name {
    position: absolute;
    left: 70px; top: 96px;
    font-family: "Montserrat", sans-serif;
    font-weight: 700;
    font-size: 26px;
    line-height: 1.05;
    color: var(--brand-blue);
    text-transform: uppercase;
    letter-spacing: 0.5px;
  }
  .contact-block {
    position: absolute;
    left: 470px; top: 62px;
    padding-left: 22px;
    border-left: 2px solid var(--rule-grey);
    font-size: 13px;
    line-height: 19px;
  }
  .contact-block .label { color: var(--label-blue); }
  .contact-block .icon { display: inline-block; width: 12px; margin-right: 5px; vertical-align: -1px; }
  .letter-body {
    position: absolute;
    left: 100px; top: 300px;
    width: 600px;
    font-size: 13.5px;
    line-height: 20px;
  }
  .letter-body p { margin-bottom: 22px; }
  .signature {
    position: absolute;
    left: 120px; top: 880px;
    width: 140px; height: 70px;
    background: #eeeef0;
  }
  .footer-band {
    position: absolute;
    left: 0; right: 0; top: 990px;
    height: 40px;
    background: var(--brand-blue);
    color: #fff;
    font-size: 15px;
    display: flex;
    align-items: center;
    justify-content: flex-end;
    padding-right: 60px;
    gap: 10px;
  }
  .footer-band .dot { display: inline-block; width: 8px; height: 8px; border-radius: 50%; background: #fff; margin-right: 6px; }
</style>
</head>
<body>
  <main class="letterhead">
    <div class="brand-name">Silver Creek<br>Plumbing</div>

    <div class="contact-block">
      <div><span class="label">ABN:</span> 47 381 905 462</div>
      <div><span class="label">PCL:</span> 5187</div>
      <div>
        <svg class="icon" viewBox="0 0 12 12"><path d="M2.5 1 L4.5 1 L5.3 3.6 L4 4.6 Q5 7 7.4 8 L8.4 6.7 L11 7.5 L11 9.5 Q11 11 9.5 11 Q1 10 1 2.5 Q1 1 2.5 1 Z" fill="var(--label-blue)"/></svg>0461 238 574
      </div>
      <div>
        <svg class="icon" viewBox="0 0 12 12"><rect x="0.5" y="2.5" width="11" height="7" fill="var(--label-blue)"/><path d="M0.5 2.5 L6 6.5 L11.5 2.5" fill="none" stroke="#fff" stroke-width="1"/></svg>enquiries@scplumbwork.net.au
      </div>
    </div>

    <section class="letter-body">
      <p>Dear customer,</p>
      <p>Lorem ipsum dolor sit amet, consectetur adipisicing elit, sed do eiusmod tempor incididunt ut labore et dolore magna aliqua. Ut enim ad minim veniam, quis nostrud exercitation ullamco laboris nisi ut aliquip ex ea commodo consequat. Duis aute irure dolor in reprehenderit in voluptate velit esse cillum dolore eu fugiat nulla pariatur. Excepteur sint occaecat cupidatat non proident, sunt in culpa qui officia deserunt mollit anim id est laborum.</p>
      <p>Lorem ipsum dolor sit amet, consectetur adipisicing elit, sed do eiusmod tempor incididunt ut labore et dolore magna aliqua. Ut enim ad minim veniam, quis nostrud exercitation ullamco laboris nisi ut aliquip ex ea commodo consequat. Duis aute irure dolor in reprehenderit in voluptate velit esse cillum dolore eu fugiat nulla pariatur. Excepteur sint occaecat cupidatat non proident, sunt in culpa qui officia deserunt mollit anim id est laborum.</p>
      <p>Lorem ipsum dolor sit amet, consectetur adipisicing elit, sed do eiusmod tempor incididunt ut labore et dolore magna aliqua. Ut enim ad minim veniam, quis nostrud exercitation ullamco laboris nisi ut aliquip ex ea commodo consequat. Duis aute irure dolor in reprehenderit in voluptate velit esse cillum dolore eu fugiat nulla pariatur. Excepteur sint occaecat cupidatat non proident, sunt in culpa qui officia deserunt mollit anim id est laborum.</p>
      <p>Lorem ipsum dolor sit amet, consectetur adipisicing elit, sed do eiusmod tempor incididunt ut labore et dolore magna aliqua. Ut enim ad minim veniam, quis nostrud exercitation ullamco laboris nisi ut aliquip ex ea commodo consequat. Duis aute irure dolor in reprehenderit.</p>
      <p>Yours Sincerely,</p>
    </section>

    <div class="signature" role="img" aria-label="Handwritten signature"></div>

    <footer class="footer-band">
      <span><span class="dot"></span>Domestic &amp; Commercial Plumbing</span>
      <span><span class="dot"></span>Tip Truck &amp; Excavator hire</span>
    </footer>
  </main>
</body>
</html>
```